New Signage Design Project for Qr Lake Facades *

Im Looking for yard design with our logo, number, website, services & credentials. Each Yard sign will be for 3 different titles...

Example 1: New Roof Coming Soon (Title) This Yardsign is for projects before we start them... Letting neighbors know why we are going to be there.
Example 2: New Roof In progress (Title) This Yardsign is for during the process of the work.. letting neighbors know what we working on!!
Example 3: This Design is only for the customer that says a title NEW ROOF INSTALL SATISFIED CUSTOMER ON THIS DESIGN I DONT NEED SERVICES JSUT LOGO AND THE TITLE

Target Market(s)

Customers

Industry/Entity Type

Roofing

Font styles to use
Serif
Sans Serif

Colors
33b8a4
5c5c5c

Requirements
Must have
• -LOGO
• -WEBSITE
• -NUMBER
• -TITLES
• -SERVICES (ROOFING, GUTTERS, PAINTING, PRESSURE WASHING, EXTERIOR DESIGN.)
• -CREDENTIALS
• -HOUSE SHAPE DESIGN
• -LOGO COLORS
• -NOT BUSY BUT CLEAN AND SHARP
• -MATTE COLORS
Nice to have
• Easy To read, Eye Catchy, Clean Design, logo colors, titles
Should not have
• not Busy,

```html
<!DOCTYPE html>
<html lang="en">
<head>
<meta charset="utf-8">
<title>Qr Lake Facades – Yard Signs</title>
<link rel="stylesheet" href="https://fonts.googleapis.com/css2?family=Anton&family=Open+Sans:wght@700;800&display=swap">
<style>
  :root {
    --teal: #0b8f80;
    --ink: #111111;
    --band-dark: #1e1e1e;
    --paper: #f7f7f7;
    --slate: #5c5c5c;
    --badge-red: #d7262c;
    --badge-blue: #1d4f91;
    --stage-edge: #6f6f6f;
    --stage-mid: #d6d6d6;
  }
  * { margin: 0; padding: 0; box-sizing: border-box; }
  html, body { width: 1200px; height: 2493px; overflow: hidden; }
  body {
    background: linear-gradient(90deg, var(--stage-edge) 0%, var(--stage-mid) 50%, var(--stage-edge) 100%);
    position: relative;
    font-family: "Open Sans", Arial, sans-serif;
  }
  .yard-sign {
    position: absolute;
    left: 103px;
    width: 992px;
    height: 743px;
    background: var(--paper);
    box-shadow: 0 6px 18px rgba(0,0,0,0.45);
    overflow: hidden;
  }
  .sign-before { top: 879px; }
  .sign-during { top: 95px; }
  .sign-after { top: 1667px; }

  .brand-name {
    position: absolute;
    left: 66px;
    top: 120px;
    width: 300px;
    color: var(--teal);
    font-weight: 800;
    font-size: 62px;
    line-height: 1.02;
    letter-spacing: -1px;
  }
  .credential {
    position: absolute;
    top: 66px;
    height: 52px;
  }
  .credential-a { left: 671px; width: 177px; background: var(--badge-red); border-top: 8px solid var(--slate); }
  .credential-b { left: 874px; top: 52px; width: 40px; height: 66px; background: var(--badge-blue); }
  .sign-after .credential-a { left: 600px; top: 74px; width: 232px; height: 62px; }
  .sign-after .credential-b { left: 862px; top: 74px; width: 52px; height: 62px; }

  .sign-title {
    position: absolute;
    left: 420px;
    right: 78px;
    top: 138px;
    text-align: right;
    font-family: "Anton", Impact, sans-serif;
    text-transform: uppercase;
    line-height: 1;
  }
  .title-lead { display: block; color: var(--teal); font-size: 116px; letter-spacing: -1px; }
  .title-sub { display: block; color: var(--ink); font-size: 88px; margin-top: 12px; letter-spacing: -1px; }
  .sign-after .sign-title { top: 190px; left: 400px; }
  .sign-after .title-lead { font-size: 66px; }
  .sign-after .title-sub { font-size: 62px; margin-top: 6px; }

  .house-band { position: absolute; left: 0; top: 0; width: 992px; height: 743px; }
  .house-band .roof { fill: var(--teal); }
  .house-band .base { fill: var(--band-dark); }

  .services {
    position: absolute;
    left: 0; right: 0;
    top: 440px;
    text-align: center;
    color: var(--ink);
    font-weight: 800;
    font-size: 27px;
    line-height: 1.25;
  }
  .phone-pill {
    position: absolute;
    left: 158px;
    top: 537px;
    width: 676px;
    height: 105px;
    border-radius: 53px;
    border: 4px solid #ffffff;
    background: var(--teal);
    color: #ffffff;
    font-weight: 700;
    font-size: 64px;
    line-height: 97px;
    text-align: center;
  }
  .web-address {
    position: absolute;
    left: 0; right: 0;
    top: 650px;
    text-align: center;
    color: #ffffff;
    font-weight: 800;
    font-size: 64px;
    line-height: 80px;
  }
</style>
</head>
<body>

  <section class="yard-sign sign-during">
    <svg class="house-band" viewBox="0 0 992 743" aria-hidden="true">
      <polygon class="roof" points="0,475 496,374 992,475 992,577 0,577"/>
      <rect class="base" x="0" y="577" width="992" height="166"/>
    </svg>
    <div class="brand-name">Qr Lake Facades</div>
    <div class="credential credential-a"></div>
    <div class="credential credential-b"></div>
    <h2 class="sign-title"><span class="title-lead">New Roof</span><span class="title-sub">In Progress</span></h2>
    <p class="services">ROOFING, GUTTERS, PAINTING,<br>PRESSURE WASHING, EXTERIOR DESIGN.</p>
    <div class="phone-pill">(555) 014-7200</div>
    <div class="web-address">qrlakefacades.com</div>
  </section>

  <section class="yard-sign sign-before">
    <svg class="house-band" viewBox="0 0 992 743" aria-hidden="true">
      <polygon class="roof" points="0,475 496,374 992,475 992,577 0,577"/>
      <rect class="base" x="0" y="577" width="992" height="166"/>
    </svg>
    <div class="brand-name">Qr Lake Facades</div>
    <div class="credential credential-a"></div>
    <div class="credential credential-b"></div>
    <h2 class="sign-title"><span class="title-lead">New Roof</span><span class="title-sub">Coming Soon</span></h2>
    <p class="services">ROOFING, GUTTERS, PAINTING,<br>PRESSURE WASHING, EXTERIOR DESIGN.</p>
    <div class="phone-pill">(555) 014-7200</div>
    <div class="web-address">qrlakefacades.com</div>
  </section>

  <section class="yard-sign sign-after">
    <svg class="house-band" viewBox="0 0 992 743" aria-hidden="true">
      <polygon class="roof" points="0,475 496,374 992,475 992,577 0,577"/>
      <rect class="base" x="0" y="577" width="992" height="166"/>
    </svg>
    <div class="brand-name">Qr Lake Facades</div>
    <div class="credential credential-a"></div>
    <div class="credential credential-b"></div>
    <h2 class="sign-title"><span class="title-lead">New Roof Install</span><span class="title-sub">Satisfied Customer</span></h2>
    <p class="services">ROOFING, GUTTERS, PAINTING,<br>PRESSURE WASHING, EXTERIOR DESIGN.</p>
    <div class="phone-pill">(555) 014-7200</div>
    <div class="web-address">qrlakefacades.com</div>
  </section>

</body>
</html>
```